Store Promo Card (already have logo!)

I need a card design (single side) for my online women’s gift shop containing a promotional code to be placed in bags for attendees at an event. I’m flexible on both shape and sizing, but perhaps a 4x6 card.
—It should contain my attached logo, my website (www.corvidtpq.com), and my Instagram handle (@corvidtpq) and promotion language such as “15% off your purchase with code: MIRVOL”.
—I think I would like my logo to be large.
—It should be clean, simple and modern in design and should use the colors from my logo.
—I would like about 3-5 product pictures depending on design.
Target Market(s)
Women ages 30 to 60
Industry/Entity Type
Retail Upscale Gift
Look and feel

```html
<!DOCTYPE html>
<html lang="en">
<head>
<meta charset="utf-8">
<title>Corvid TPQ – Promo Card</title>
<link rel="stylesheet" href="https://fonts.googleapis.com/css2?family=Abril+Fatface&family=Montserrat:wght@500&display=swap">
<style>
  :root {
    --ink: #5f6160;
    --rose: #f2a79c;
    --rose-soft: #f7d3cd;
    --wood: #e4e2e8;
    --wash: #f3eff2;
  }
  * { margin: 0; padding: 0; box-sizing: border-box; }
  html, body { width: 1200px; height: 800px; overflow: hidden; background: var(--wash); }
  .card {
    position: relative;
    width: 1200px;
    height: 800px;
    overflow: hidden;
    font-family: "Abril Fatface", serif;
    color: var(--ink);
  }
  .card__photo {
    position: absolute;
    inset: 0;
    background:
      radial-gradient(ellipse 380px 300px at 260px 500px, var(--rose-soft), transparent 70%),
      radial-gradient(ellipse 420px 260px at 620px 130px, var(--rose-soft), transparent 70%),
      radial-gradient(ellipse 300px 260px at 1050px 150px, var(--rose-soft), transparent 70%),
      linear-gradient(170deg, var(--wash) 0%, var(--wood) 45%, #eceaf0 75%, #f6f4f8 100%);
  }
  .promo-headline {
    position: absolute;
    top: 30px;
    left: 0;
    width: 100%;
    text-align: center;
    font-size: 158px;
    line-height: 1;
    letter-spacing: 2px;
  }
  .brand-frame {
    position: absolute;
    left: 64px;
    top: 202px;
    width: 1072px;
    height: 373px;
    border: 4px solid var(--ink);
  }
  .brand-name {
    position: absolute;
    top: 270px;
    left: 0;
    width: 100%;
    text-align: center;
    font-size: 196px;
    line-height: 1;
    letter-spacing: 4px;
  }
  .contact {
    position: absolute;
    top: 540px;
    font-size: 26px;
    line-height: 1;
    letter-spacing: 0.5px;
  }
  .contact--web { left: 87px; }
  .contact--social {
    right: 93px;
    display: flex;
    align-items: center;
    gap: 8px;
  }
  .contact__mark {
    width: 20px;
    height: 20px;
    background: var(--ink);
    border-radius: 5px;
  }
  .promo-code {
    position: absolute;
    top: 658px;
    left: 0;
    width: 100%;
    text-align: center;
    font-size: 54px;
    line-height: 1;
    letter-spacing: 1px;
  }
</style>
</head>
<body>
  <main class="card">
    <div class="card__photo" role="img" aria-label="Soft photograph of coral pink roses lying on pale whitewashed wooden boards"></div>

    <h1 class="promo-headline">15% OFF</h1>

    <div class="brand-frame"></div>
    <p class="brand-name">CORVID</p>

    <p class="contact contact--web">WWW.CORVIDTPQ.COM</p>
    <p class="contact contact--social"><span class="contact__mark"></span>@CORVIDTPQ</p>

    <p class="promo-code">YOUR PURCHASE WITH CODE: MIRVOL</p>
  </main>
</body>
</html>
```